Modern looking signage for dental office.

Exterior signage for passing cars
Target Market(s)
Cars passing by
Font styles to use
Sans Serif
Colors
3276b5
Requirements
Must have
- Logo
- OPEN ON SUTURDAY AND SUNDAY
- NIGHT CLINIC AVAILABLE
- PLEASE USE THE FONT TYPE IN FILE 4 UPLOADED BELOW.
- (482) 730-2964
- Modern looking

```html
<!DOCTYPE html>
<html lang="en">
<head>
<meta charset="utf-8">
<title>Nova Dental – Exterior Sign</title>
<link rel="stylesheet" href="https://fonts.googleapis.com/css2?family=Montserrat:wght@300&family=Encode+Sans+Semi+Condensed:wght@400&family=Open+Sans:ital,wght@0,700;1,700&display=swap">
<style>
  :root {
    --teal: #07849e;
    --teal-deep: #05606f;
    --teal-text: #0a7f94;
    --panel: #ffffff;
    --ink: #56504f;
    --tooth-tint: #d7edf1;
  }
  html, body {
    margin: 0;
    padding: 0;
    width: 1200px;
    height: 800px;
    overflow: hidden;
    background: var(--teal);
  }
  .sign {
    display: block;
    width: 1200px;
    height: 800px;
  }
  .sign-frame { fill: var(--teal); }
  .sign-panel { fill: var(--panel); }
  .sign-shadow { fill: var(--teal-deep); }
  .banner { fill: var(--teal); }
  .brand-ring { fill: none; stroke: var(--ink); stroke-width: 3; }
  .brand-name {
    font-family: "Montserrat", sans-serif;
    font-weight: 300;
    font-size: 112px;
    fill: var(--ink);
  }
  .tagline {
    font-family: "Encode Sans Semi Condensed", sans-serif;
    font-weight: 400;
    font-size: 46px;
    fill: var(--ink);
  }
  .tooth-area { fill: var(--tooth-tint); }
  .open-word {
    font-family: "Open Sans", sans-serif;
    font-style: italic;
    font-weight: 700;
    font-size: 76px;
    fill: var(--teal-text);
  }
  .open-on, .open-days {
    font-family: "Open Sans", sans-serif;
    font-weight: 700;
    fill: var(--teal-text);
  }
  .open-on { font-size: 46px; }
  .open-days { font-size: 42px; }
  .night-clinic {
    font-family: "Open Sans", sans-serif;
    font-style: italic;
    font-weight: 700;
    font-size: 86px;
    fill: var(--panel);
  }
  .phone {
    font-family: "Open Sans", sans-serif;
    font-weight: 700;
    font-size: 132px;
    fill: var(--ink);
  }
</style>
</head>
<body>
<svg class="sign" viewBox="0 0 1200 800" xmlns="http://www.w3.org/2000/svg">
  <rect class="sign-frame" x="0" y="0" width="1200" height="800"/>

  <!-- shadows along banner edge and lower curve -->
  <path class="sign-shadow" d="M622,418 H640 L576,610 H558 Z"/>
  <path class="sign-shadow" d="M1138,610 H1150 Q1096,748 936,768 H928 Q1080,740 1138,610 Z"/>

  <!-- white panel -->
  <path class="sign-panel" d="M22,19 H1160 V418 H632 L568,610 H1138 Q1080,740 928,764 H22 Z"/>

  <!-- banner -->
  <path class="banner" d="M640,418 H1160 V610 H576 Z"/>

  <!-- brand -->
  <g class="brand">
    <circle class="brand-ring" cx="170" cy="188" r="116"/>
    <text class="brand-name" x="312" y="238" textLength="832" lengthAdjust="spacingAndGlyphs">NOVA DENTAL</text>
    <text class="tagline" x="394" y="312" textLength="640" lengthAdjust="spacingAndGlyphs">MODERN GENERAL DENTISTRY</text>
  </g>

  <!-- hours -->
  <g class="hours">
    <rect class="tooth-area" x="38" y="374" width="160" height="226" rx="40" role="img" aria-label="Tooth outline illustration"/>
    <text class="open-word" x="152" y="516" textLength="200" lengthAdjust="spacingAndGlyphs">Open</text>
    <text class="open-on" x="364" y="516">on</text>
    <text class="open-days" x="146" y="574" textLength="416" lengthAdjust="spacingAndGlyphs">Saturday &amp; Sunday</text>
  </g>

  <!-- night clinic -->
  <g class="night">
    <text class="night-clinic" x="640" y="494" textLength="452" lengthAdjust="spacingAndGlyphs">Night Clinic</text>
    <text class="night-clinic" x="696" y="584" textLength="368" lengthAdjust="spacingAndGlyphs">available</text>
  </g>

  <!-- phone -->
  <text class="phone" x="74" y="724" textLength="856" lengthAdjust="spacingAndGlyphs">(482) 730-2964</text>
</svg>
</body>
</html>
```